ASSET BASED PROGRAM FLIER

Need flier to market hard money loan products offered HARD MONEY FIX & FLIP PROGRAMS

We offer a variety of loan programs Some program highlights include......

1) No Minimum Credit Score
2) 3-5 Day Close
3) Up to 100% of Purchase & Rehab
4) Rates as Low as 7%
5) Loans Offered Nationwide

Contact us today for more information at (800) 647-2915 x42 or email us at mwelton@brightlanefunding.example NMLS #731856 www.brightlanefunding.example

```html
<!DOCTYPE html>
<html lang="en">
<head>
<meta charset="utf-8">
<title>Hard Money Fix &amp; Flip Programs Flier</title>
<link rel="stylesheet" href="https://fonts.googleapis.com/css2?family=Source+Sans+3:wght@400;600;700&family=Montserrat:wght@400&display=swap">
<style>
  :root {
    --page-bg: #f4f4f4;
    --paper: #ffffff;
    --brand-blue: #0a5ea8;
    --sand: #e2dcb4;
    --gold: #b39a2c;
    --ink: #2f2f2f;
    --ink-soft: #555555;
    --photo-sky: #d4d6e8;
    --photo-mid: #b9a98a;
    --photo-ground: #6f7458;
  }
  * { margin: 0; padding: 0; box-sizing: border-box; }
  html, body {
    width: 1200px; height: 1200px; overflow: hidden;
    background: var(--page-bg);
  }
  .flier-frame {
    position: absolute; left: 190px; top: 22px;
    width: 820px; height: 1157px;
    background: var(--paper);
    overflow: hidden;
  }
  .flier {
    position: absolute; left: 0; top: 0;
    width: 990px; height: 1397px;
    transform: scale(0.8283);
    transform-origin: 0 0;
    font-family: "Source Sans 3", sans-serif;
    color: var(--ink);
  }
  .hero-art { position: absolute; left: 0; top: 0; width: 990px; height: 900px; }
  .badge-new {
    position: absolute; left: 673px; top: 47px;
    width: 234px; height: 234px; border-radius: 50%;
    background: var(--brand-blue); color: #fff;
    text-align: center;
  }
  .badge-new .big { display: block; margin-top: 34px; font-size: 74px; font-weight: 600; letter-spacing: 6px; line-height: 1; }
  .badge-new .small { display: block; font-size: 30px; letter-spacing: 4px; line-height: 1.2; }
  .program-title {
    position: absolute; left: 73px; top: 604px; width: 324px;
    text-align: center; color: #fff;
    font-size: 51px; font-weight: 600; line-height: 50px;
  }
  .brand-mark {
    position: absolute; left: 118px; top: 990px;
    display: flex; align-items: center; gap: 14px;
  }
  .brand-mark .dot { width: 34px; height: 34px; border-radius: 50%; background: var(--brand-blue); }
  .brand-mark .name { font-size: 34px; font-weight: 600; color: var(--brand-blue); letter-spacing: 1px; }
  .contact { position: absolute; left: 93px; top: 1132px; }
  .contact h2 { font-size: 31px; font-weight: 700; line-height: 1; color: #222; }
  .contact .lead { font-size: 16px; color: var(--ink-soft); margin-top: 6px; }
  .contact .rule { width: 56px; height: 1px; background: #bbb; margin: 12px 0 8px; }
  .contact .phone {
    font-family: "Montserrat", sans-serif; font-size: 31px; color: var(--gold);
    display: flex; align-items: center; gap: 6px;
  }
  .contact .line {
    font-family: "Montserrat", sans-serif; font-size: 19px; color: #333;
    display: flex; align-items: center; gap: 10px; margin-top: 4px;
  }
  .divider { position: absolute; left: 548px; top: 917px; width: 2px; height: 380px; background: var(--gold); }
  .highlights { position: absolute; left: 600px; top: 918px; list-style: none; }
  .highlights li {
    position: relative; padding-left: 24px;
    font-size: 27px; font-weight: 600; line-height: 50px; color: var(--ink);
  }
  .highlights li::before { content: "•"; position: absolute; left: 2px; }
  .highlights .cont { display: block; padding-left: 36px; }
</style>
</head>
<body>
  <div class="flier-frame">
    <div class="flier">
      <svg class="hero-art" viewBox="0 0 990 900" aria-hidden="false">
        <defs>
          <linearGradient id="photoTones" x1="0" y1="0" x2="0.3" y2="1">
            <stop offset="0" stop-color="var(--photo-sky)"/>
            <stop offset="0.5" stop-color="var(--photo-mid)"/>
            <stop offset="1" stop-color="var(--photo-ground)"/>
          </linearGradient>
        </defs>
        <path class="sand-swoosh" fill="var(--sand)"
          d="M380 110 C470 80 540 90 545 150 C700 160 860 230 920 330 C990 450 950 640 840 730 C720 825 520 830 420 790 C300 740 140 700 70 600 C40 520 60 420 120 300 C200 170 300 120 380 110 Z"/>
        <path class="hero-photo" role="img" aria-label="Photo of a smiling construction worker in a yellow hard hat carrying lumber on his shoulder"
          fill="url(#photoTones)"
          d="M330 102 C480 95 560 150 555 165 C720 180 880 270 925 390 C960 520 880 700 720 770 C620 800 500 790 445 780 C380 640 300 570 150 560 C70 540 38 470 42 400 C55 230 190 110 330 102 Z"/>
        <path class="program-blob" fill="var(--brand-blue)"
          d="M240 542 C320 535 352 560 355 600 C358 650 340 690 375 740 C405 790 380 860 300 878 C220 895 120 870 85 800 C55 735 75 640 130 590 C165 560 200 545 240 542 Z"/>
      </svg>

      <div class="badge-new"><span class="big">NEW</span><span class="small">LOAN<br>PROGRAMS</span></div>

      <h1 class="program-title">HARD<br>MONEY<br>FIX &amp; FLIP<br>PROGRAMS</h1>

      <div class="brand-mark"><span class="dot"></span><span class="name">Brightlane Funding</span></div>

      <div class="contact">
        <h2>QUESTION ?</h2>
        <p class="lead">FEEL FREE TO CONTACT US..</p>
        <div class="rule"></div>
        <p class="phone">
          <svg width="28" height="28" viewBox="0 0 24 24" aria-hidden="true"><path fill="var(--gold)" d="M6.6 10.8a15.1 15.1 0 0 0 6.6 6.6l2.2-2.2c.3-.3.7-.4 1-.2 1.1.4 2.3.6 3.6.6.6 0 1 .4 1 1V20c0 .6-.4 1-1 1A17 17 0 0 1 3 4c0-.6.4-1 1-1h3.5c.6 0 1 .4 1 1 0 1.3.2 2.5.6 3.6.1.3 0 .7-.2 1l-2.3 2.2z"/></svg>
          (800) 647-2915 EXT. 42
        </p>
        <p class="line">
          <svg width="20" height="16" viewBox="0 0 20 16" aria-hidden="true"><rect x="0" y="0" width="20" height="16" fill="#333"/><path d="M1 1l9 7 9-7" stroke="#fff" stroke-width="1.6" fill="none"/></svg>
          mwelton@brightlanefunding.example
        </p>
        <p class="line">
          <svg width="20" height="18" viewBox="0 0 20 18" aria-hidden="true"><path fill="#333" d="M10 0l10 9h-3v9h-5v-6H8v6H3V9H0z"/></svg>
          www.brightlanefunding.example
        </p>
      </div>

      <div class="divider"></div>

      <ul class="highlights">
        <li>NO MINIMUM CREDIT<span class="cont">SCORE</span></li>
        <li>3-5 DAY CLOSE</li>
        <li>UP TO 100% OF<span class="cont">PURCHASE &amp; REHAB</span></li>
        <li>RATES AS LOW AS 7%</li>
        <li>LOANS OFFERED<span class="cont">NATIONWIDE</span></li>
      </ul>
    </div>
  </div>
</body>
</html>
```